Personal Trainer Business Card Design and Logo

I am a Personal Trainer and passionate in helping obese kids loose weight, I would love a business card design for my business called LORK Fitness.
LORK Ftiness stands for Lively Origami Running Kicks, I would like the business card to be bright and appealing to the kids as well as the parents.
I would also love a logo designs witch is simple but affective.

Things I would like in the business card
- Kids playing and being happy (no cartoon characters)
- The card should be bright and colourful
- My name, Bartholomew Van Rijk Personal Trainer
- Contact number 0472618059
- Email address lorkfitness@mailzorp.com

Things I would like in the logo
-colourful design which incorporate kids
- your creative logo

thanks for all your entries
kind regards Bart

loving all the designs, you are all so talented.

could you please read the updated brief

kind regards

Bart

Reason: Loving the designs, but needs more modification kind reagrds Bart

Target Market(s)

Kids and Parents

Industry/Entity Type

Business

Contact Information for Business Card

LORK Fitness for kids

Lively Origami Running Kicks

Bart Van Rijk Personal Trainer
0472618059

Requirements
Must have
• Kids laughing and happy, lork fitness logo, Bart Van Rijk Personal Trainer, 0472618059,lorkfitness@mailzorp.com, colourful and bright.
Nice to have
• pulsewell council tick

```html
<!DOCTYPE html>
<html lang="en">
<head>
<meta charset="utf-8">
<title>LORK Fitness – Business Card</title>
<link href="https://fonts.googleapis.com/css2?family=Arimo:wght@400;700&display=swap" rel="stylesheet">
<style>
  :root {
    --canvas-bg: #f4f4f6;
    --card-pink: #f7d6e6;
    --card-white: #ffffff;
    --brand-purple: #6a2c91;
    --name-crimson: #e0134f;
    --logo-orange: #f29a1f;
    --photo-warm: #f0c24a;
    --photo-cool: #7fb6d9;
    --card-shadow: rgba(0, 0, 0, 0.18);
  }
  * { box-sizing: border-box; margin: 0; padding: 0; }
  html, body {
    width: 1200px;
    height: 900px;
    overflow: hidden;
    background: var(--canvas-bg);
    font-family: "Arimo", Arial, sans-serif;
  }
  .card-pair {
    position: absolute;
    top: 290px;
    left: 40px;
    display: flex;
    gap: 40px;
  }
  .business-card {
    width: 540px;
    height: 320px;
    border-radius: 26px;
    background:
      radial-gradient(circle at 15% 85%, rgba(255,255,255,0.7) 0 60px, transparent 61px),
      radial-gradient(circle at 88% 15%, rgba(255,255,255,0.6) 0 45px, transparent 46px),
      linear-gradient(135deg, var(--card-pink) 0%, var(--card-white) 45%, var(--card-white) 60%, var(--card-pink) 100%);
    box-shadow: 0 18px 30px var(--card-shadow);
    display: flex;
    flex-direction: column;
    align-items: center;
    position: relative;
  }
  .brand-mark {
    display: flex;
    align-items: center;
    gap: 10px;
    color: var(--logo-orange);
    font-weight: 700;
    text-transform: uppercase;
    letter-spacing: 1px;
  }
  .brand-mark .brand-dot {
    border-radius: 50%;
    background: var(--logo-orange);
  }
  /* Front */
  .card-front .brand-mark { margin-top: 48px; font-size: 42px; }
  .card-front .brand-dot { width: 28px; height: 28px; }
  .kids-photo {
    margin-top: 16px;
    width: 230px;
    height: 120px;
    border-radius: 10px;
    background: linear-gradient(90deg, var(--photo-warm), var(--photo-cool) 55%, var(--photo-warm));
  }
  .tagline {
    margin-top: 18px;
    color: var(--brand-purple);
    font-size: 17px;
    letter-spacing: 3.5px;
  }
  /* Back */
  .card-back .brand-mark { margin-top: 50px; font-size: 24px; }
  .card-back .brand-dot { width: 16px; height: 16px; }
  .trainer-name {
    margin-top: 36px;
    color: var(--name-crimson);
    font-size: 24px;
    font-weight: 700;
  }
  .trainer-role {
    margin-top: 6px;
    color: var(--brand-purple);
    font-size: 18px;
    font-weight: 700;
  }
  .contact-list {
    list-style: none;
    margin-top: 26px;
    text-align: center;
    color: var(--brand-purple);
    font-size: 19px;
    font-weight: 700;
    line-height: 1.35;
  }
</style>
</head>
<body>
  <main class="card-pair">
    <section class="business-card card-front">
      <div class="brand-mark"><span class="brand-name">LORK Fitness</span><span class="brand-dot"></span></div>
      <div class="kids-photo" role="img" aria-label="Photo of a group of happy children jumping with arms raised"></div>
      <p class="tagline">Lively Origami Running Kicks</p>
    </section>
    <section class="business-card card-back">
      <div class="brand-mark"><span class="brand-name">LORK Fitness</span><span class="brand-dot"></span></div>
      <h1 class="trainer-name">Bart Van Rijk</h1>
      <p class="trainer-role">Personal Trainer</p>
      <ul class="contact-list">
        <li class="contact-phone">0472618059</li>
        <li class="contact-email">lorkfitness@mailzorp.com</li>
      </ul>
    </section>
  </main>
</body>
</html>
```